Boutique Financial Services/Advisor Business Needs Web Design

Looking for an informational and functional web design for my Financial Services/Financial Advisement business. It should have functionality for Company name, address, phone #, "About Us", Who we are, Our Mission, Services we offer, Biographies/Photos of/about "The Team", and possibly a link to "Contact Us". Would like to see something new & exciting blended with a traditional/professional look that will appeal to those approaching retirement, as well as those younger clients that are beginning to think about planning for the future. I already have a web domain through HostMeadow, but would like this to be the design we use for that domain.
Financial Services/Financial Advisor
Coded - Design and coding required
1 page

```html
<!DOCTYPE html>
<html lang="en">
<head>
<meta charset="utf-8">
<title>Summitrise Wealth Management</title>
<link href="https://fonts.googleapis.com/css2?family=Poppins:wght@300;400;500;600;700;800&display=swap" rel="stylesheet">
<style>
:root{
  --blue:#0a4ea8;
  --blue-mid:#1a6fc4;
  --blue-soft:#7ea9d9;
  --pale:#e8f0f8;
  --ink:#111;
  --gold:#d9b21c;
  --white:#fff;
  --line:#e6ebf1;
}
*{box-sizing:border-box;margin:0;padding:0}
html,body{width:1200px;height:1200px;overflow:hidden;background:#fff;font-family:'Poppins',sans-serif;color:var(--ink)}
.page{position:absolute;left:349px;top:0;width:806px;height:1932px;transform:scale(0.6211);transform-origin:0 0;background:#fff;overflow:hidden}
.abs{position:absolute}
.header{left:0;top:0;width:806px;height:68px;background:var(--pale)}
.brand-box{left:30px;top:10px;width:85px;height:48px;background:#fff;border:1px solid #c9d6e6;display:flex;align-items:center;justify-content:center;text-align:center;font-size:7px;font-weight:600;color:var(--blue);line-height:1.2}
.nav a{position:absolute;top:31px;font-size:6.5px;font-weight:600;color:var(--blue);text-decoration:none;white-space:nowrap}
.chip{top:12px;height:16px;background:var(--blue);color:#fff;font-size:6px;display:flex;align-items:center;gap:4px;padding:0 5px;white-space:nowrap}
.hero{left:0;top:68px;width:806px;height:292px;background:linear-gradient(120deg,#4a5563 0%,#2f3e52 30%,#5f7fa3 60%,#c6d3e0 85%,#e6ecf2 100%)}
.hero-welcome{left:0;width:806px;top:88px;text-align:center;font-size:29px;font-weight:300;color:#fff}
.hero-title{left:0;width:806px;text-align:center;font-size:27px;font-weight:800;color:var(--gold);letter-spacing:.5px}
.hero-copy{left:220px;width:366px;top:210px;text-align:center;font-size:8px;font-weight:700;color:#fff;letter-spacing:1.6px;line-height:12px}
.btn{background:var(--blue);color:#fff;font-size:8px;letter-spacing:2.5px;display:flex;align-items:center;justify-content:center;height:23px;width:116px}
.h2{font-size:14px;font-weight:700}
.blue{color:var(--blue-mid)}
.navy{color:var(--blue)}
.small{font-size:6.5px;line-height:10.5px}
.mission{left:0;top:538px;width:806px;height:274px;background:var(--pale)}
.pill{left:40px;width:329px;height:28px;border-radius:14px;background:var(--blue-soft);display:flex;align-items:center;gap:7px;padding-left:8px;color:#fff;font-size:6px;font-weight:600}
.pill svg{flex:none}
.photo{border:3px solid #fff;box-shadow:0 0 4px rgba(0,0,0,.15)}
.card{width:231px;border:1px solid #9bbbe0;background:var(--pale)}
.card h3{position:absolute;left:17px;top:26px;font-size:8.5px;font-weight:700}
.card p{position:absolute;left:17px;top:38px;width:200px;font-size:6.3px;line-height:10.5px}
.icon{width:46px;height:46px;border-radius:50%;background:var(--blue-mid);border:2px solid #fff}
.team-card{width:231px;height:131px;background:var(--pale);top:1155px;text-align:center}
.team-card .name{position:absolute;top:49px;width:100%;font-size:8.5px;font-weight:700}
.team-card .role{position:absolute;top:63px;width:100%;font-size:8.5px}
.team-card .bio{position:absolute;top:78px;left:17px;width:200px;text-align:left;font-size:6.3px;line-height:10.5px;color:#333}
.portrait{width:96px;height:90px;border-radius:50%;top:1105px}
.divider{left:0;width:806px;height:1px;background:var(--line)}
.label{left:380px;font-size:7.5px}
.field{left:455px;width:242px;border:1px solid #e0e4ea;font-size:6.5px;color:#888;padding:9px 7px;background:#fff}
.footer h4{font-size:9.5px;font-weight:600;color:#fff}
.footer li{list-style:none;font-size:6.5px;color:#fff;line-height:12px}
</style>
</head>
<body>
<div class="page">
  <div class="abs header"></div>
  <div class="abs brand-box">Summitrise Wealth<br>Management</div>
  <nav class="nav">
    <a style="left:226px">About Us</a>
    <a style="left:297px">Our Mision</a>
    <a style="left:368px">Services we offer</a>
    <a style="left:440px">Our The Team</a>
    <a style="left:511px">Contact Us</a>
  </nav>
  <div class="abs chip" style="left:610px;width:73px">
    <svg width="6" height="6" viewBox="0 0 10 10"><path d="M2 1l2 2-1 1.5c.8 1.5 1.5 2.2 3 3L7.5 6l2 2-1.5 1.5C4 9 1 6 .5 2.5z" fill="#fff"/></svg>+100 2468 1357</div>
  <div class="abs chip" style="left:694px;width:76px">
    <svg width="7" height="6" viewBox="0 0 10 8"><rect width="10" height="8" fill="#fff"/><path d="M0 0l5 4 5-4" stroke="#0a4ea8" fill="none"/></svg>hi@summitrise.co</div>

  <div class="abs hero" role="img" aria-label="Photo of a hand holding a pen over financial charts and a keyboard"></div>
  <svg class="abs" style="left:0;top:300px" width="806" height="70" viewBox="0 0 806 70">
    <path d="M0 50 C200 20 400 60 560 58 C680 56 760 35 806 28 L806 70 L0 70Z" fill="#fff"/>
    <path d="M0 52 C200 22 400 62 560 60 C680 58 760 37 806 30" stroke="#1a6fc4" stroke-width="6" fill="none"/>
  </svg>
  <div class="abs hero-welcome">Welcome to</div>
  <div class="abs hero-title" style="top:131px">SUMMITRISE WEALTH</div>
  <div class="abs hero-title" style="top:172px">MANAGEMENT</div>
  <div class="abs hero-copy">Lorem ipsum dolor sit amet consectetur adipisicing consequatur quos sed fugiat ducimus, fuga iusto laboriosam ex! Dolorem alias sint neque consequuntur architecto maxime fugiat possimus?</div>
  <div class="abs btn" style="left:350px;top:271px;width:106px">Read more</div>

  <div class="abs" role="img" aria-label="Photo of a smiling business team around a table" style="left:46px;top:382px;width:288px;height:144px;background:linear-gradient(135deg,#cfd7df,#8c98a6 50%,#e9edf1)"></div>
  <div class="abs h2" style="left:369px;top:405px">Who <span class="blue">We are</span></div>
  <p class="abs small navy" style="left:369px;top:429px;width:384px;text-align:justify">Lorem ipsum dolor sit amet, consectetur adipisicing elit. Exercitationem, porro? Praesentium minus aspernatur doloribus nulla animi excepturi unde! Delectus similique nam amet corporis debitis dolorem tenetur blanditiis. Culpa laudantium eos sed a illum molestiae adipisci iusto, aut, magnam esse quaerat saepe eligendi? Laudantium facilis placeat nemo ratione dignissimos ipsum dicta.</p>
  <div class="abs btn" style="left:369px;top:478px">Read more</div>

  <div class="abs mission"></div>
  <div class="abs photo" role="img" aria-label="Photo of glass office towers against a blue sky" style="left:538px;top:510px;width:152px;height:196px;background:linear-gradient(180deg,#9cc3e6,#4f79a8 60%,#6fae3c)"></div>
  <div class="abs photo" role="img" aria-label="Photo of a modern suburban house" style="left:484px;top:582px;width:90px;height:124px;background:linear-gradient(180deg,#d99ab0,#8e7a6c 55%,#6d8f4a)"></div>
  <div class="abs photo" role="img" aria-label="Photo of a stock market trading screen" style="left:658px;top:544px;width:100px;height:162px;background:linear-gradient(160deg,#1c2433,#2e4866 60%,#0e1420)"></div>
  <div class="abs h2 navy" style="left:40px;top:565px">Our mission</div>
  <p class="abs small" style="left:40px;top:599px;width:404px;text-align:justify;color:#444">&emsp;&emsp;&nbsp;Lorem ipsum dolor sit amet consectetur adipisicing elit. Sed aperiam in, iusto et voluptatem, quia maiores cum architecto facere blanditiis reiciendis modi explicabo tempora minima maxime dignissimos unde necessitatibus? Maxime?</p>
  <div class="abs pill" style="top:652px"><svg width="18" height="18" viewBox="0 0 18 18"><circle cx="9" cy="9" r="9" fill="#fff"/><path d="M5 9.5l2.6 2.5L13 6.5" stroke="#1a6fc4" stroke-width="1.8" fill="none"/></svg>Lorem ipsum dolor sit amet consectetur adipisicing elit. Sed aperiam in</div>
  <div class="abs pill" style="top:686px"><svg width="18" height="18" viewBox="0 0 18 18"><circle cx="9" cy="9" r="9" fill="#fff"/><path d="M5 9.5l2.6 2.5L13 6.5" stroke="#1a6fc4" stroke-width="1.8" fill="none"/></svg>Lorem ipsum dolor sit amet consectetur adipisicing elit. Sed aperiam in</div>
  <div class="abs pill" style="top:719px"><svg width="18" height="18" viewBox="0 0 18 18"><circle cx="9" cy="9" r="9" fill="#fff"/><path d="M5 9.5l2.6 2.5L13 6.5" stroke="#1a6fc4" stroke-width="1.8" fill="none"/></svg>Lorem ipsum dolor sit amet consectetur adipisicing elit. Sed aperiam in</div>
  <div class="abs btn" style="left:40px;top:768px">Read more</div>

  <div class="abs h2 navy" style="left:0;width:806px;top:842px;text-align:center">Our Services</div>
  <div class="abs" style="left:0;width:806px;top:868px;text-align:center;font-size:5.5px">Our financial services are a sector that provides financial services</div>
  <div class="abs card" style="left:40px;top:906px;height:88px"><h3>Investment</h3><p>Lorem ipsum dolor sit amet, consectetur adipisicing elit. Quia voluptatem facilis ipsam fugit, aliquam corrupti asperiores laborum quibusdam quidem mollitia.</p></div>
  <div class="abs card" style="left:288px;top:906px;height:88px"><h3>Credit or financing</h3><p>Lorem ipsum dolor sit amet, consectetur adipisicing elit. Quia voluptatem facilis ipsam fugit, aliquam corrupti asperiores laborum quibusdam quidem mollitia.</p></div>
  <div class="abs card" style="left:536px;top:906px;height:88px"><h3>Financing other</h3><p>Lorem ipsum dolor sit amet, consectetur adipisicing elit. Quia voluptatem facilis ipsam fugit, aliquam corrupti asperiores laborum quibusdam quidem mollitia.</p></div>
  <svg class="abs icon" style="left:173px;top:885px" viewBox="0 0 46 46"><g fill="#fff"><ellipse cx="23" cy="15" rx="10" ry="4"/><ellipse cx="23" cy="22" rx="10" ry="4"/><ellipse cx="23" cy="29" rx="10" ry="4"/></g></svg>
  <svg class="abs icon" style="left:421px;top:885px" viewBox="0 0 46 46"><path d="M18 12h10l-3 5c6 3 9 8 9 13 0 4-5 6-11 6s-11-2-11-6c0-5 3-10 9-13z" fill="#fff"/><text x="23" y="32" font-size="11" font-weight="700" text-anchor="middle" fill="#1a6fc4" font-family="Poppins,sans-serif">$</text></svg>
  <svg class="abs icon" style="left:668px;top:885px" viewBox="0 0 46 46"><circle cx="19" cy="19" r="9" fill="#fff"/><circle cx="28" cy="27" r="9" fill="#fff" stroke="#1a6fc4" stroke-width="1.5"/><text x="19" y="23" font-size="10" font-weight="700" text-anchor="middle" fill="#1a6fc4" font-family="Poppins,sans-serif">$</text></svg>

  <div class="abs divider" style="top:1030px"></div>

  <div class="abs h2 blue" style="left:0;width:806px;top:1061px;text-align:center">The team</div>
  <div class="abs" style="left:0;width:806px;top:1082px;text-align:center;font-size:6px">Our financial team are a sector that provides financial team</div>
  <div class="abs team-card" style="left:40px"><div class="name">Mr. Daniel Hartwell</div><div class="role">Chief financial officer (CFO)</div><div class="bio">A senior executive who oversees all financial and accounting activities, including financial planning, transaction tracking, and strategy consulting</div></div>
  <div class="abs team-card" style="left:288px"><div class="name">Miss. Elena Voss</div><div class="role">Financial analyst</div><div class="bio">Analyzes financial information and provides financial advice to companies and organizations. They use data sets like market trends.</div></div>
  <div class="abs team-card" style="left:536px"><div class="name">Mis. Clara Linden</div><div class="role">Accountant</div><div class="bio">Collects and analyzes financial data for companies or individuals. They ensure that records are complete and accurate</div></div>
  <div class="abs portrait" role="img" aria-label="Portrait photo of the chief financial officer" style="left:106px;background:radial-gradient(circle at 50% 40%,#b7b9bd,#5f6369 70%,#eef0f3)"></div>
  <div class="abs portrait" role="img" aria-label="Portrait photo of the financial analyst" style="left:353px;background:radial-gradient(circle at 50% 40%,#d8b393,#8e6a4c 70%,#c9b9a6)"></div>
  <div class="abs portrait" role="img" aria-label="Portrait photo of the accountant" style="left:600px;background:radial-gradient(circle at 50% 40%,#e0b08e,#7a5a3e 70%,#3d4b3a)"></div>

  <div class="abs divider" style="top:1330px"></div>

  <div class="abs" style="left:96px;width:170px;top:1518px;text-align:center;font-size:11px;font-weight:600;color:var(--blue);line-height:1.2">Summitrise Wealth<br>Management</div>
  <div class="abs" style="left:60px;width:242px;top:1552px;text-align:center;font-size:7.8px;line-height:12.2px;color:#222">
    <div><svg width="8" height="8" viewBox="0 0 10 10"><path d="M2 1l2 2-1 1.5c.8 1.5 1.5 2.2 3 3L7.5 6l2 2-1.5 1.5C4 9 1 6 .5 2.5z" fill="#111"/></svg> +100 246 135</div>
    <div><svg width="8" height="7" viewBox="0 0 10 8"><rect width="10" height="8" fill="#111"/><path d="M0 0l5 4 5-4" stroke="#fff" fill="none"/></svg> hi@summitrise.co</div>
    <div>Harbour Lane, Seabrook NSW 2990, <b>Australia</b></div>
    <div>PO BOX 208 Ridgeford SA 5901, <b>Australia</b></div>
  </div>
  <div class="abs" style="left:363px;top:1390px;width:1px;height:300px;background:var(--line)"></div>
  <div class="abs" style="left:400px;width:252px;top:1393px;text-align:center;font-size:13px;font-weight:600">Contact Us</div>
  <div class="abs label" style="top:1433px">First Name</div>
  <div class="abs label" style="top:1471px">Last Name</div>
  <div class="abs label" style="top:1508px">Country</div>
  <div class="abs label" style="top:1595px">Subject</div>
  <div class="abs field" style="top:1425px;height:25px;padding-top:7px">Your name..</div>
  <div class="abs field" style="top:1464px;height:25px;padding-top:7px">Your last name..</div>
  <div class="abs field" style="top:1503px;height:25px;padding-top:7px;color:#222;display:flex;justify-content:space-between">Australia<span>&#8964;</span></div>
  <div class="abs field" style="top:1542px;height:115px">Write something..</div>
  <div class="abs btn" style="left:455px;top:1667px">Submit</div>

  <svg class="abs" style="left:0;top:1725px" width="806" height="80" viewBox="0 0 806 80">
    <path d="M0 45 C150 10 320 15 480 35 C640 55 740 30 806 18 L806 80 L0 80Z" fill="#0a4ea8"/>
    <path d="M0 58 C160 22 330 28 490 45 C650 62 740 40 806 26" stroke="#fff" stroke-width="5" fill="none"/>
    <path d="M0 40 C150 5 320 10 480 30 C640 50 740 25 806 12" stroke="#1a6fc4" stroke-width="6" fill="none"/>
  </svg>
  <div class="abs footer" style="left:0;top:1800px;width:806px;height:132px;background:var(--blue)">
    <div class="abs" style="left:98px;top:18px;width:115px;height:56px;background:#fff;border:3px solid #fff;outline:1px solid var(--blue);outline-offset:-5px;display:flex;align-items:center;justify-content:center;text-align:center;font-size:8px;font-weight:600;color:var(--blue);line-height:1.2">Summitrise Wealth<br>Management</div>
    <h4 class="abs" style="left:319px;top:19px">Address</h4>
    <div class="abs" style="left:319px;top:39px;font-size:5px;line-height:8.3px;color:#fff">
      <div>+100 246 135</div><div>hi@summitrise.co</div><div>Harbour Lane, Seabrook NSW 2990,</div><div><b>Australia</b></div><div>PO BOX 208 Ridgeford SA 5901,</div><div><b>Australia</b></div>
    </div>
    <h4 class="abs" style="left:487px;top:19px">Menu</h4>
    <ul class="abs" style="left:487px;top:40px"><li>Home</li><li>Services</li><li>Our Team</li><li>contact Us</li></ul>
    <h4 class="abs" style="left:655px;top:18px;font-size:8px">Social Media</h4>
    <svg class="abs" style="left:655px;top:43px" width="75" height="18" viewBox="0 0 75 18">
      <circle cx="9" cy="9" r="8" fill="#fff"/><circle cx="37" cy="9" r="8" fill="#fff"/><circle cx="64" cy="9" r="8" fill="#fff"/>
    </svg>
  </div>
</div>
</body>
</html>
```